Silver Ridge Business Card Design

I have an existing corporate logo. I'd like to clean it up bit (sharpen it up) and make it look better (without major redesign). I'd like to get the logo itself in all major file formats for print, web, etc.
Then I'd like a business card design that reflects a strategy consulting firm. It should be clean - logo and text without major graphics, and perhaps some small color treatments that match the logo color. The card should suggest high quality in terms of the company.
I'd like the files for card in all major print formats.
Target Market(s)
Silver Ridge Partners is a strategy development and business consulting firm focused on small to mid-sized companies. We specialize in business strategy, comprehensive business plan development, market segmentation and positioning, financial models, marketing and sales strategy, product strategy and the effective use of social media in business growth. We operate as consultants, advisers, retained members of management teams, and Board members. We often serve in the role of Chief Strategy Officer, supporting CEO's and other senior executives to enhance top and bottom line growth.
Our overall approach with clients is to deliver actual results, and we often take an active team role with business founders and management teams to drive business growth and affect real changes in performance. As a result, we approach each situation uniquely and partner with clients in a manner that will have the biggest impact on enterprise value.
Business
Look and feel

```html
<!DOCTYPE html>
<html lang="en">
<head>
<meta charset="utf-8">
<title>Silver Ridge Partners — Business Card</title>
<link rel="stylesheet" href="https://fonts.googleapis.com/css2?family=Montserrat:wght@400;600;700&display=swap">
<style>
  :root {
    --page-bg: #e6e7ea;
    --card-white: #ffffff;
    --card-mist: #eef0f3;
    --brand-blue: #3d5591;
    --brand-blue-soft: #8fa0c6;
    --ink: #1f2533;
    --ink-muted: #5b6170;
    --shadow: rgba(20, 28, 45, 0.18);
  }
  * { box-sizing: border-box; margin: 0; padding: 0; }
  html, body {
    width: 1200px; height: 900px; overflow: hidden;
    background: var(--page-bg);
    font-family: "Montserrat", Arial, sans-serif;
  }
  .canvas {
    position: relative; width: 1200px; height: 900px;
  }
  .card {
    position: absolute; left: 340px; width: 520px; height: 297px;
    border-radius: 4px; overflow: hidden;
    background: var(--card-white);
    box-shadow: 0 14px 34px var(--shadow);
  }
  .card--back { top: 110px; }
  .card--front {
    top: 490px;
    background: radial-gradient(ellipse at 55% 50%, var(--card-white) 0%, var(--card-white) 35%, var(--card-mist) 100%);
  }
  .card__band { position: absolute; inset: 0; width: 100%; height: 100%; }

  .holder {
    position: absolute; top: 22px; left: 150px; text-align: center;
  }
  .holder__name {
    font-weight: 700; font-size: 19px; letter-spacing: 0.5px;
    color: var(--brand-blue); text-transform: uppercase;
  }
  .holder__title {
    font-weight: 400; font-size: 11px; letter-spacing: 1.5px;
    color: var(--ink-muted); text-transform: uppercase; margin-top: 2px;
  }

  .contact-list {
    position: absolute; left: 36px; top: 178px; list-style: none;
  }
  .contact-list__item {
    display: flex; align-items: flex-start; gap: 14px;
    font-size: 12.5px; line-height: 1.35; letter-spacing: 0.8px;
    color: var(--ink-muted); text-transform: uppercase;
    margin-bottom: 9px;
  }
  .contact-list__icon { width: 18px; height: 18px; flex: none; margin-top: 0; }

  .wordmark {
    position: absolute; inset: 0;
    display: flex; align-items: center; justify-content: center; gap: 16px;
  }
  .wordmark__dot {
    width: 22px; height: 22px; border-radius: 50%; background: var(--brand-blue);
  }
  .wordmark__name {
    font-weight: 600; font-size: 24px; line-height: 1.15; letter-spacing: 1px;
    color: var(--ink); text-transform: uppercase;
  }
</style>
</head>
<body>
<main class="canvas">

  <section class="card card--back" aria-label="Business card back">
    <svg class="card__band" viewBox="0 0 520 297" aria-hidden="true">
      <path d="M0 172 Q 300 150 430 0 L 520 0 L 520 28 Q 430 165 0 182 Z" fill="var(--brand-blue)"/>
      <path d="M300 120 Q 420 80 470 0 L 488 0 Q 440 90 300 120 Z" fill="var(--brand-blue-soft)" opacity="0.5"/>
    </svg>

    <header class="holder">
      <h1 class="holder__name">Daniel Morrow</h1>
      <p class="holder__title">Consultant</p>
    </header>

    <ul class="contact-list">
      <li class="contact-list__item">
        <svg class="contact-list__icon" viewBox="0 0 24 24" aria-hidden="true">
          <path fill="var(--brand-blue)" d="M6.6 10.8a15 15 0 0 0 6.6 6.6l2.2-2.2a1 1 0 0 1 1-.25 11.4 11.4 0 0 0 3.6.57 1 1 0 0 1 1 1V20a1 1 0 0 1-1 1A17 17 0 0 1 3 4a1 1 0 0 1 1-1h3.5a1 1 0 0 1 1 1c0 1.25.2 2.45.57 3.57a1 1 0 0 1-.25 1z"/>
        </svg>
        <span>(212) 555.0148</span>
      </li>
      <li class="contact-list__item">
        <svg class="contact-list__icon" viewBox="0 0 24 24" aria-hidden="true">
          <rect x="2.5" y="5.5" width="19" height="13" fill="none" stroke="var(--brand-blue)" stroke-width="1.8"/>
          <polyline points="2.5,5.5 12,13 21.5,5.5" fill="none" stroke="var(--brand-blue)" stroke-width="1.8"/>
        </svg>
        <span>info@silverridgepartners.com</span>
      </li>
      <li class="contact-list__item">
        <svg class="contact-list__icon" viewBox="0 0 24 24" aria-hidden="true">
          <path fill="var(--brand-blue)" d="M12 2a7 7 0 0 0-7 7c0 5.2 7 13 7 13s7-7.8 7-13a7 7 0 0 0-7-7zm0 9.5A2.5 2.5 0 1 1 12 6.5a2.5 2.5 0 0 1 0 5z"/>
        </svg>
        <span>Mercer Lane<br>Albany, NY 12207, USA</span>
      </li>
    </ul>
  </section>

  <section class="card card--front" aria-label="Business card front">
    <div class="wordmark">
      <span class="wordmark__dot" aria-hidden="true"></span>
      <p class="wordmark__name">Silver Ridge<br>Partners, LLC</p>
    </div>
  </section>

</main>
</body>
</html>
```